Label Design for Amber Reed Specialty Coffee Roasters

We are a specialty coffee beans Roasting Shop named "Amber Reed". We pack our beans in stand up poaches of varying sizes. We sell beans both to B2C and B2B and are looking to design stickers that will stand out. Our logo was designed with a black and white background. So far, we have been using white glossy bean bags and came up with a front label design that we would like to use for our labels.
We would like to see the design tweaked to fit both a white bag and a black one.
Currently, the attached front label design does not work on white bags. We would also like to have a back sticker designed that needs to include: 1- a description section for the type of beans used 2- a QR code section

Target Market(s)

Specialty beans in our area are typically liked by the younger generations 40 years and younger. Both male and females drink our coffee with varying income levels. But generally, middle class and above buy our coffee beans.

Requirements
Must have
• We are am looking for a sticker to be placed on a coffee bean bag. The sticker needs to contain the roasting shop's logo and brand name "Amber Reed". Also, the sticker needs to have the following: country name, bean variety, weight (kg), roast date. The sticker needs to have the following specifications on a 5 point Likert scale (Strength, Fruitiness, Earthiness, Brightness). I uploaded a front label design that needs to be tweaked to fit both a white bag and a black one. The current design has owls representing the 5 point Likert scale and part of the shop's logo. We would like to keep that part of the design if possible. Currently, the attached front label design does not work on white bags.
We would also like to have a back sticker designed that needs to include: 1- a description section for the type of beans used 2- a QR code section
Nice to have
• The font that is used in the logo is League Gothic. It is okay to use this font or any other font if you find it more appropriate for the design.

```html
<!DOCTYPE html>
<html lang="en">
<head>
<meta charset="utf-8">
<title>Amber Reed – Colombia front label</title>
<link href="https://fonts.googleapis.com/css2?family=League+Gothic&family=Montserrat:wght@400;600&display=swap" rel="stylesheet">
<style>
  :root {
    --backdrop: #a38f62;
    --bag-white: #ececec;
    --bag-black: #121212;
    --label-paper: #f1f1f1;
    --ink: #1b1b1b;
    --band: #4a4a4a;
    --band-light: #5a5a5a;
    --muted: #c9c9c9;
    --paper-text: #ffffff;
  }
  * { margin: 0; padding: 0; box-sizing: border-box; }
  html, body { width: 1200px; height: 900px; overflow: hidden; }
  body { background: var(--backdrop); position: relative; font-family: "Montserrat", sans-serif; }

  .bag { position: absolute; border-radius: 6px; }
  .bag--white { left: 259px; top: 155px; width: 324px; height: 453px; background: var(--bag-white); }
  .bag--black { left: 610px; top: 273px; width: 324px; height: 454px; background: var(--bag-black); }
  .bag__zip { position: absolute; left: 0; right: 0; top: 48px; height: 2px; opacity: .25; }
  .bag--white .bag__zip { background: #9a9a9a; }
  .bag--black .bag__zip { background: #4a4a4a; }

  .label { position: absolute; width: 240px; height: 320px; }
  .bag--white .label { left: 42px; top: 110px; }
  .bag--black .label { left: 42px; top: 103px; }
  .label svg { width: 100%; height: 100%; display: block; overflow: visible; }

  .label__arc-text { font-family: "Montserrat", sans-serif; font-size: 6px; letter-spacing: 1.9px; fill: var(--ink); }
  .label__brand { font-family: "League Gothic", sans-serif; font-size: 30px; fill: var(--ink); }
  .label__origin { font-family: "League Gothic", sans-serif; font-size: 48px; fill: var(--paper-text); letter-spacing: .5px; }
  .label__variety { font-family: "Montserrat", sans-serif; font-size: 6.5px; letter-spacing: 4px; fill: var(--paper-text); }
  .label__spec { font-family: "Montserrat", sans-serif; font-size: 6.3px; fill: var(--ink); }
  .label__meta { font-family: "Montserrat", sans-serif; font-size: 5.4px; fill: var(--ink); }
  .label__meta--bold { font-weight: 600; }
</style>
</head>
<body>

<div class="bag bag--white">
  <div class="bag__zip"></div>
  <div class="label">
    <svg viewBox="0 0 240 320" aria-label="Amber Reed Colombia label for white bag">
      <defs>
        <path id="arc-white" d="M36 56 Q120 26 204 56"/>
      </defs>
      <path d="M8 36 Q120 -4 232 36 L232 140 L238 175 L232 210 L232 272 Q205 314 120 318 Q35 314 8 272 L8 210 L2 175 L8 140 Z" fill="var(--label-paper)" stroke="var(--ink)" stroke-width="1.4"/>
      <path d="M13 40 Q120 3 227 40 L227 140 L227 270 Q200 308 120 312 Q40 308 13 270 L13 140 Z" fill="none" stroke="var(--ink)" stroke-width="1.8"/>
      <text class="label__arc-text" text-anchor="middle"><textPath href="#arc-white" startOffset="50%">SPECIALTY COFFEE ROASTERS</textPath></text>
      <circle cx="66" cy="96" r="7" fill="var(--ink)"/>
      <text class="label__brand" x="128" y="106" text-anchor="middle">AMBER REED</text>
      <rect role="img" aria-label="Dark grey chevron pattern band" x="13" y="143" width="214" height="68" fill="var(--band)"/>
      <path d="M2 175 L-6 172 L-10 175 L-6 178 Z M238 175 L246 172 L250 175 L246 178 Z" fill="var(--ink)"/>
      <text class="label__origin" x="120" y="193" text-anchor="middle">COLOMBIA</text>
      <text class="label__variety" x="120" y="206" text-anchor="middle">VARIETY</text>
      <g class="label__spec" text-anchor="end">
        <text x="90" y="234">STRENGTH</text>
        <text x="90" y="245">FRUITNESS</text>
        <text x="90" y="256">EARTHINESS</text>
        <text x="90" y="267">BRIGHTNESS</text>
      </g>
      <g>
        <circle cx="98" cy="232" r="2.3" fill="var(--ink)"/><circle cx="105" cy="232" r="2.3" fill="var(--ink)"/><circle cx="112" cy="232" r="2.3" fill="var(--ink)"/><circle cx="119" cy="232" r="2.3" fill="var(--muted)"/><circle cx="126" cy="232" r="2.3" fill="var(--muted)"/>
        <circle cx="98" cy="243" r="2.3" fill="var(--ink)"/><circle cx="105" cy="243" r="2.3" fill="var(--muted)"/><circle cx="112" cy="243" r="2.3" fill="var(--muted)"/><circle cx="119" cy="243" r="2.3" fill="var(--muted)"/><circle cx="126" cy="243" r="2.3" fill="var(--muted)"/>
        <circle cx="98" cy="254" r="2.3" fill="var(--ink)"/><circle cx="105" cy="254" r="2.3" fill="var(--ink)"/><circle cx="112" cy="254" r="2.3" fill="var(--ink)"/><circle cx="119" cy="254" r="2.3" fill="var(--muted)"/><circle cx="126" cy="254" r="2.3" fill="var(--muted)"/>
        <circle cx="98" cy="265" r="2.3" fill="var(--ink)"/><circle cx="105" cy="265" r="2.3" fill="var(--ink)"/><circle cx="112" cy="265" r="2.3" fill="var(--ink)"/><circle cx="119" cy="265" r="2.3" fill="var(--muted)"/><circle cx="126" cy="265" r="2.3" fill="var(--muted)"/>
      </g>
      <line x1="139" y1="223" x2="139" y2="273" stroke="var(--ink)" stroke-width=".6"/>
      <text class="label__meta" x="170" y="231" text-anchor="middle">Weight</text>
      <text class="label__meta label__meta--bold" x="170" y="238" text-anchor="middle">60kg</text>
      <line x1="152" y1="243" x2="192" y2="243" stroke="var(--ink)" stroke-width=".5"/>
      <text class="label__meta" x="168" y="252" text-anchor="middle">Roast Date</text>
      <text class="label__meta label__meta--bold" x="168" y="259" text-anchor="middle">20 | 2 | 2020</text>
      <path role="img" aria-label="Grey chevron pattern strip" d="M38 290 L202 290 Q175 306 120 308 Q65 306 38 290 Z" fill="var(--band-light)"/>
    </svg>
  </div>
</div>

<div class="bag bag--black">
  <div class="bag__zip"></div>
  <div class="label">
    <svg viewBox="0 0 240 320" aria-label="Amber Reed Colombia label for black bag">
      <defs>
        <path id="arc-black" d="M36 56 Q120 26 204 56"/>
      </defs>
      <path d="M8 36 Q120 -4 232 36 L232 140 L238 175 L232 210 L232 272 Q205 314 120 318 Q35 314 8 272 L8 210 L2 175 L8 140 Z" fill="var(--label-paper)" stroke="var(--ink)" stroke-width="1.4"/>
      <path d="M13 40 Q120 3 227 40 L227 140 L227 270 Q200 308 120 312 Q40 308 13 270 L13 140 Z" fill="none" stroke="var(--ink)" stroke-width="1.8"/>
      <text class="label__arc-text" text-anchor="middle"><textPath href="#arc-black" startOffset="50%">SPECIALTY COFFEE ROASTERS</textPath></text>
      <circle cx="66" cy="96" r="7" fill="var(--ink)"/>
      <text class="label__brand" x="128" y="106" text-anchor="middle">AMBER REED</text>
      <rect role="img" aria-label="Dark grey chevron pattern band" x="13" y="143" width="214" height="68" fill="var(--band)"/>
      <path d="M2 175 L-6 172 L-10 175 L-6 178 Z M238 175 L246 172 L250 175 L246 178 Z" fill="var(--paper-text)"/>
      <text class="label__origin" x="120" y="193" text-anchor="middle">COLOMBIA</text>
      <text class="label__variety" x="120" y="206" text-anchor="middle">VARIETY</text>
      <g class="label__spec" text-anchor="end">
        <text x="90" y="234">STRENGTH</text>
        <text x="90" y="245">FRUITNESS</text>
        <text x="90" y="256">EARTHINESS</text>
        <text x="90" y="267">BRIGHTNESS</text>
      </g>
      <g>
        <circle cx="98" cy="232" r="2.3" fill="var(--ink)"/><circle cx="105" cy="232" r="2.3" fill="var(--ink)"/><circle cx="112" cy="232" r="2.3" fill="var(--ink)"/><circle cx="119" cy="232" r="2.3" fill="var(--muted)"/><circle cx="126" cy="232" r="2.3" fill="var(--muted)"/>
        <circle cx="98" cy="243" r="2.3" fill="var(--ink)"/><circle cx="105" cy="243" r="2.3" fill="var(--muted)"/><circle cx="112" cy="243" r="2.3" fill="var(--muted)"/><circle cx="119" cy="243" r="2.3" fill="var(--muted)"/><circle cx="126" cy="243" r="2.3" fill="var(--muted)"/>
        <circle cx="98" cy="254" r="2.3" fill="var(--ink)"/><circle cx="105" cy="254" r="2.3" fill="var(--ink)"/><circle cx="112" cy="254" r="2.3" fill="var(--ink)"/><circle cx="119" cy="254" r="2.3" fill="var(--muted)"/><circle cx="126" cy="254" r="2.3" fill="var(--muted)"/>
        <circle cx="98" cy="265" r="2.3" fill="var(--ink)"/><circle cx="105" cy="265" r="2.3" fill="var(--ink)"/><circle cx="112" cy="265" r="2.3" fill="var(--ink)"/><circle cx="119" cy="265" r="2.3" fill="var(--muted)"/><circle cx="126" cy="265" r="2.3" fill="var(--muted)"/>
      </g>
      <line x1="139" y1="223" x2="139" y2="273" stroke="var(--ink)" stroke-width=".6"/>
      <text class="label__meta" x="170" y="231" text-anchor="middle">Weight</text>
      <text class="label__meta label__meta--bold" x="170" y="238" text-anchor="middle">60kg</text>
      <line x1="152" y1="243" x2="192" y2="243" stroke="var(--ink)" stroke-width=".5"/>
      <text class="label__meta" x="168" y="252" text-anchor="middle">Roast Date</text>
      <text class="label__meta label__meta--bold" x="168" y="259" text-anchor="middle">20 | 2 | 2020</text>
      <path role="img" aria-label="Grey chevron pattern strip" d="M38 290 L202 290 Q175 306 120 308 Q65 306 38 290 Z" fill="var(--band-light)"/>
    </svg>
  </div>
</div>

</body>
</html>
```